Tallowmere Roofing Business Card

Need a business card with the logo that was designed here

Contact Information for Business Card

Name, Title, Phone, Email, Website, Company name

```html
<!DOCTYPE html>
<html lang="en">
<head>
<meta charset="utf-8">
<title>Tallowmere Roofing Business Card</title>
<link rel="stylesheet" href="https://fonts.googleapis.com/css2?family=Montserrat:wght@400;500;700&display=swap">
<style>
  :root {
    --page: #c9c9c9;
    --card: #7b7b7b;
    --card-deep: #747474;
    --blue: #3f78c9;
    --white: #ffffff;
    --silver: #d6d6d6;
  }
  * { box-sizing: border-box; margin: 0; padding: 0; }
  html, body { width: 1200px; height: 788px; overflow: hidden; }
  body {
    background: var(--page);
    font-family: "Montserrat", Arial, sans-serif;
    display: flex;
    align-items: center;
    justify-content: center;
    gap: 40px;
  }
  .card {
    position: relative;
    width: 540px;
    height: 309px;
    border-radius: 18px;
    background: var(--card);
    overflow: hidden;
  }
  .corner-mark {
    position: absolute;
    top: 0;
    right: 34px;
    width: 26px;
    height: 22px;
    background: var(--blue);
  }
  .holder {
    position: absolute;
    top: 38px;
    right: 70px;
    text-align: right;
  }
  .holder-name {
    color: var(--blue);
    font-weight: 700;
    font-size: 21px;
    letter-spacing: 1.5px;
  }
  .holder-title {
    color: var(--white);
    font-size: 11px;
    margin-top: 3px;
  }
  .brand {
    position: absolute;
    left: 34px;
    top: 112px;
    display: flex;
    align-items: center;
    gap: 8px;
    color: var(--white);
    font-weight: 700;
    font-size: 20px;
    letter-spacing: 0.5px;
  }
  .brand-square {
    width: 12px;
    height: 12px;
    background: var(--white);
  }
  .contact {
    position: absolute;
    left: 34px;
    bottom: 28px;
    color: var(--white);
    font-size: 12.5px;
    line-height: 1.5;
  }
  .address { margin-bottom: 12px; }
  .contact-line { display: flex; align-items: center; gap: 8px; }
  .contact-line svg { width: 11px; height: 11px; fill: var(--blue); flex: none; }
  .card-back .brand {
    position: absolute;
    left: 0; right: 0; top: 0; bottom: 0;
    justify-content: center;
    color: var(--silver);
    font-size: 30px;
    gap: 12px;
  }
  .card-back .brand-square { width: 16px; height: 16px; background: var(--silver); }
</style>
</head>
<body>
  <section class="card card-front">
    <div class="corner-mark"></div>
    <div class="holder">
      <p class="holder-name">CORWIN HALLOWAY</p>
      <p class="holder-title">Managing Director</p>
    </div>
    <div class="brand"><span class="brand-square"></span>Tallowmere Roofing</div>
    <div class="contact">
      <p class="address">418 Ferncliff Road<br>Ashgrove County 5170</p>
      <p class="contact-line">
        <svg viewBox="0 0 12 12"><path d="M2.5 1 L4.5 1 L5.2 3.6 L3.9 4.6 Q5 7 7.4 8.1 L8.4 6.8 L11 7.5 L11 9.5 Q10.5 11 9 11 Q1 10 1 3 Q1 1.5 2.5 1 Z"/></svg>
        0412 555 019
      </p>
      <p class="contact-line">
        <svg viewBox="0 0 12 12"><path d="M1 2.5 H11 V9.5 H1 Z M1.6 3 L6 6.4 L10.4 3 V3.2 L6 7.2 L1.6 3.2 Z" fill-rule="evenodd"/></svg>
        info@tallowmereroofing.com
      </p>
      <p class="contact-line">
        <svg viewBox="0 0 12 12"><circle cx="6" cy="6" r="5"/></svg>
        www.tallowmereroofing.com
      </p>
    </div>
  </section>
  <section class="card card-back">
    <div class="brand"><span class="brand-square"></span>Tallowmere Roofing</div>
  </section>
</body>
</html>
```